Educational Agency in Abu Dhabi looking for an 8 pages website

We are looking for an 8 pages design for a website, we already have one but we need to refine it and it is www.korvalendi.ae - Please base it on logo colours (attached) I have uploaded our logo, website content logo colors to use it for the scheme.
We are looking for a smooth look and content added if possible, I also attached content and logo

Industry/Entity Type

Education

Coding

Coded - Design and coding required

Number of Pages Required

5+ page

```html
<!DOCTYPE html>
<html lang="en">
<head>
<meta charset="utf-8">
<title>Korvalendi – Study Abroad Advisors</title>
<link href="https://fonts.googleapis.com/css2?family=Lato:wght@300;400;700&family=Libre+Baskerville:wght@400;700&family=Questrial&display=swap" rel="stylesheet">
<style>
:root{
  --navy:#1f2d6b;
  --navy-dark:#17235a;
  --footer:#1c2b6a;
  --footer-bottom:#16224f;
  --blue:#1b6cbd;
  --green:#9dc33b;
  --ink:#222;
  --text:#555;
  --muted:#777;
  --line:#d9d9d9;
  --soft:#f3f3f3;
  --white:#fff;
  --star:#f0a830;
}
*{margin:0;padding:0;box-sizing:border-box}
html,body{width:1200px;height:3593px;overflow:hidden}
body{font-family:"Questrial",Arial,sans-serif;color:var(--text);background:var(--white);position:relative}
.abs{position:absolute}
a{color:inherit;text-decoration:none}

/* header */
.site-header{position:absolute;top:0;left:0;width:1200px;height:156px;background:var(--white)}
.brand{position:absolute;left:91px;top:40px;display:flex;align-items:center;gap:12px}
.brand-mark{width:30px;height:30px;background:var(--navy)}
.brand-name{font-family:"Lato",sans-serif;font-weight:700;font-size:26px;color:var(--navy);letter-spacing:1px}
.call{position:absolute;right:96px;top:52px;font-family:"Lato",sans-serif;font-size:23px;color:var(--ink)}
.socials{position:absolute;right:96px;top:90px;display:flex;gap:8px}
.socials span{width:26px;height:26px;border:2px solid var(--blue);border-radius:50%;display:block}

.main-nav{position:absolute;top:156px;left:0;width:1200px;height:50px;background:var(--navy)}
.main-nav ul{list-style:none;display:flex;position:absolute;left:108px;top:0;height:50px;align-items:center;gap:38px}
.main-nav li{font-family:"Lato",sans-serif;font-weight:700;font-size:14px;color:var(--white);letter-spacing:.3px}
.login{position:absolute;left:982px;top:0;width:122px;height:50px;background:var(--green);color:var(--white);font-family:"Lato",sans-serif;font-weight:700;font-size:14px;display:flex;align-items:center;justify-content:center;gap:8px}

/* hero */
.hero{position:absolute;top:206px;left:0;width:1200px;height:436px}
.hero-photo{position:absolute;inset:0;background:linear-gradient(90deg,#7a5a45 0%,#b08a72 30%,#8c6b5a 55%,#5c4a45 75%,#3a3f6a 100%)}
.hero-shade{position:absolute;inset:0;background:rgba(20,20,30,.35)}
.hero-text{position:absolute;left:0;width:1200px;text-align:center;color:var(--white)}
.hero-kicker{top:90px;font-family:"Libre Baskerville",serif;font-size:30px}
.hero-title{top:128px;font-family:"Libre Baskerville",serif;font-weight:700;font-size:38px}
.hero-desc{top:200px;font-size:15px;line-height:24px}
.btn-green{position:absolute;left:510px;top:261px;width:177px;height:53px;background:var(--green);color:var(--white);font-family:"Lato",sans-serif;font-weight:700;font-size:13px;display:flex;align-items:center;justify-content:center}

/* who */
.who{position:absolute;top:642px;left:0;width:1200px;height:670px;background:var(--white)}
.section-title{font-family:"Lato",sans-serif;font-weight:300;color:var(--ink)}
.who h2{position:absolute;left:96px;top:92px;font-size:44px}
.who .lead{position:absolute;left:103px;top:146px;font-size:16px;color:var(--ink)}
.who p.body{position:absolute;left:103px;width:600px;font-size:13.5px;line-height:25px;color:var(--muted)}
.btn-blue{position:absolute;background:var(--blue);color:var(--white);font-family:"Lato",sans-serif;font-weight:700;font-size:13px;display:flex;align-items:center;justify-content:center}
.contact-frame{position:absolute;left:800px;top:69px;width:314px;height:506px;background:linear-gradient(180deg,#6f8fb5,#3d5f8c 60%,#2d4a78)}
.contact-card{position:absolute;left:19px;top:14px;width:276px;height:478px;background:var(--white);padding:34px 19px}
.contact-card h3{font-family:"Libre Baskerville",serif;font-weight:400;font-size:24px;color:var(--ink)}
.contact-card .hint{font-size:12px;line-height:19px;color:var(--muted);margin-top:14px}
.field{border:1px solid var(--line);height:40px;margin-top:12px;font-size:12px;color:var(--muted);padding:11px 10px}
.field.first{margin-top:20px}
.field.msg{height:82px}
.submit{margin-top:16px;height:40px;background:#222;color:var(--white);font-family:"Lato",sans-serif;font-weight:700;font-size:14px;display:flex;align-items:center;justify-content:center}

/* destinations */
.destinations{position:absolute;top:1312px;left:0;width:1200px;height:664px;background:var(--soft)}
.destinations h2{position:absolute;left:93px;top:62px;font-size:40px}
.dest-card{position:absolute;width:314px;height:192px;overflow:hidden}
.dest-card .bg{position:absolute;inset:0;background:linear-gradient(135deg,#5a5560,#3f4048 60%,#2e3038)}
.dest-card .name{position:absolute;left:34px;top:46px;font-family:"Lato",sans-serif;font-size:27px;color:var(--white)}
.dest-card .btn-blue{left:34px;top:126px;width:108px;height:34px;font-size:11px}

/* why */
.why{position:absolute;top:1976px;left:0;width:1200px;height:640px}
.why h2{position:absolute;left:0;width:1200px;top:72px;text-align:center;font-size:40px}
.why .vline{position:absolute;left:596px;top:160px;width:1px;height:435px;background:var(--line)}
.why .hline{position:absolute;left:96px;top:390px;width:1008px;height:1px;background:var(--line)}
.reason{position:absolute;width:380px}
.reason .num{position:absolute;left:0;top:0;width:38px;height:38px;border-radius:50%;background:var(--navy);color:var(--white);font-family:"Lato",sans-serif;font-weight:700;font-size:16px;display:flex;align-items:center;justify-content:center}
.reason h3{margin-left:62px;font-family:"Lato",sans-serif;font-weight:700;font-size:19px;line-height:26px;color:var(--ink)}
.reason p{margin-left:62px;margin-top:18px;font-size:13px;line-height:23px;color:var(--muted);width:290px}

/* testimonials */
.testimonials{position:absolute;top:2616px;left:0;width:1200px;height:540px}
.testimonials h2{position:absolute;left:0;width:1200px;top:32px;text-align:center;font-family:"Libre Baskerville",serif;font-weight:400;font-size:32px;color:var(--ink)}
.testimonials .rule{position:absolute;top:54px;width:80px;height:2px;background:#555}
.testimonials .sub{position:absolute;left:0;width:1200px;top:100px;text-align:center;font-size:13.5px;line-height:22px;color:var(--ink)}
.review{position:absolute;top:169px;height:173px;border:1px solid var(--line);padding:22px 28px}
.review .site{font-size:14px;color:var(--muted)}
.review .stars{color:var(--star);font-size:12px;margin-left:6px;letter-spacing:1px}
.review .who-name{font-size:14px;color:var(--muted);margin-top:2px}
.review p{margin-top:22px;font-family:"Lato",sans-serif;font-weight:700;font-size:13.5px;line-height:21px;color:var(--ink)}
.badge{position:absolute;top:397px;background:#d5d9e4}

/* footer */
.site-footer{position:absolute;top:3157px;left:0;width:1200px;height:388px;background:var(--footer);color:#c8cde0}
.foot-logo{position:absolute;left:177px;top:76px;width:129px;height:132px;background:var(--white);display:flex;align-items:center;justify-content:center;font-family:"Lato",sans-serif;font-weight:700;font-size:18px;color:var(--navy);letter-spacing:1px}
.foot-about{position:absolute;left:177px;top:226px;width:210px;font-size:13px;line-height:20px}
.foot-col{position:absolute;top:100px}
.foot-col h4{font-family:"Lato",sans-serif;font-weight:700;font-size:17px;color:var(--white);margin-bottom:12px}
.foot-col ul{list-style:none}
.foot-col li{font-size:13px;line-height:25px}
.foot-social{display:flex;gap:8px}
.foot-social span{width:28px;height:28px;border:2px solid var(--white);border-radius:50%;display:block}
.newsletter{position:absolute;left:824px;top:198px;width:187px;height:46px;border-radius:23px;background:var(--blue);color:var(--white);font-family:"Lato",sans-serif;font-weight:700;font-size:14px;display:flex;align-items:center;justify-content:center}
.footer-bottom{position:absolute;top:3545px;left:0;width:1200px;height:48px;background:var(--footer-bottom);color:#aab2cc;font-size:12px;display:flex;align-items:center;justify-content:center}
</style>
</head>
<body>

<header class="site-header">
  <div class="brand"><span class="brand-mark"></span><span class="brand-name">KORVALENDI</span></div>
  <div class="call">Call Us: (877) 555-0143</div>
  <div class="socials"><span></span><span></span><span></span><span></span></div>
</header>

<nav class="main-nav">
  <ul>
    <li>HOME</li><li>ABOUT US</li><li>PRACTICE AREAS</li><li>ATTORNEYS</li><li>LOCATIONS</li><li>CONTACT US</li>
  </ul>
  <a class="login">
    <svg width="14" height="14" viewBox="0 0 14 14" fill="none" stroke="#fff" stroke-width="1.5"><rect x="2.5" y="6" width="9" height="7"/><path d="M4.5 6V4a2.5 2.5 0 0 1 5 0v2"/></svg>
    LOG IN
  </a>
</nav>

<section class="hero">
  <div class="hero-photo" role="img" aria-label="Photo of smiling students, one wearing a graduation cap"></div>
  <div class="hero-shade"></div>
  <div class="hero-text hero-kicker abs">Welcome to</div>
  <div class="hero-text hero-title abs">International Legal Advisors</div>
  <div class="hero-text hero-desc abs">Our Primary goal has always been to Provide knowledgeable and effective legal Representation.<br>We are afforded the ability to approach our clients' cases with skill and wisdom.</div>
  <a class="btn-green">CONTACT WITH US</a>
</section>

<section class="who">
  <h2 class="section-title">Who We are</h2>
  <div class="lead">We have hands-on experience helping to grow and manage Companies</div>
  <p class="body" style="top:196px">As a firm of attorneys all with senior in-house experience, we have hands-on experience helping to grow and manage companies, ranging from start-ups seeking growth capital to publicly traded multi-nationals expanding into emerging markets. We have broad, in-depth knowledge that comes from years spent not just as outside lawyers helping clients on discreet legal matters, but also as senior business executives and in-house counsel helping companies achieve their overall business goals and objectives.</p>
  <p class="body" style="top:370px">Given the increasing legal and regulatory complexity of today's business environment, many companies are faced with the choice of either committing more and more resources to pay escalating outside counsel fees, or of taking on additional headcount and the associated fixed costs to build or expand an in-house legal department. What we offer is a third, better option: a cost-effective way to retain the services of senior, partner-level attorneys that can provide or supplement your in-house legal support on a flexible part-time, project, or interim basis.</p>
  <a class="btn-blue" style="left:103px;top:548px;width:175px;height:51px">LEARN MORE</a>

  <div class="contact-frame" role="img" aria-label="Blue city skyline photo framing the contact form">
    <form class="contact-card">
      <h3>Contact us</h3>
      <div class="hint">Please fill out the form below and one of our attorneys will contact you.</div>
      <div class="field first">Name*</div>
      <div class="field">Email*</div>
      <div class="field">Phone*</div>
      <div class="field msg">Message*</div>
      <div class="submit">SUBMIT</div>
    </form>
  </div>
</section>

<section class="destinations">
  <h2 class="section-title">Study Destinations</h2>
  <div class="dest-card" style="left:96px;top:144px"><div class="bg" role="img" aria-label="Photo of a student with the UK flag"></div><div class="name">Study in UK</div><a class="btn-blue">LEARN MORE</a></div>
  <div class="dest-card" style="left:443px;top:144px"><div class="bg" role="img" aria-label="Photo of a student with the US flag"></div><div class="name">Study in USA</div><a class="btn-blue">LEARN MORE</a></div>
  <div class="dest-card" style="left:798px;top:144px"><div class="bg" role="img" aria-label="Photo of a stack of books"></div><div class="name">Study in Australia</div><a class="btn-blue">LEARN MORE</a></div>
  <div class="dest-card" style="left:96px;top:369px"><div class="bg" role="img" aria-label="Photo of students studying together"></div><div class="name">Study in Europe</div><a class="btn-blue">LEARN MORE</a></div>
  <div class="dest-card" style="left:443px;top:369px"><div class="bg" role="img" aria-label="Photo of a student on campus"></div><div class="name">Study in Malaysia</div><a class="btn-blue">LEARN MORE</a></div>
  <div class="dest-card" style="left:798px;top:369px"><div class="bg" role="img" aria-label="Photo of students in a lecture hall"></div><div class="name">Study in Germany</div><a class="btn-blue">LEARN MORE</a></div>
</section>

<section class="why">
  <h2 class="section-title">Why Choose Korvalendi</h2>
  <div class="vline"></div>
  <div class="hline"></div>
  <div class="reason" style="left:190px;top:206px"><span class="num">1.</span><h3>Experienced Counselling &amp; Advice Based On You</h3><p>As a firm of attorneys all with senior in-house experience, we have hands-on experience helping to grow and manage companies, from start-ups seekingpublicly traded markets.</p></div>
  <div class="reason" style="left:636px;top:206px"><span class="num">2.</span><h3>Partenship with Global Network</h3><p>As a firm of attorneys all with senior in-house experience, we have hands-on experience helping to grow and manage companies, from start-ups seekingpublicly traded.</p></div>
  <div class="reason" style="left:190px;top:420px"><span class="num">3.</span><h3>Wide range of Country</h3><p>As a firm of attorneys all with senior in-house experience, we have hands-on experience helping to grow and manage companies, from start-ups seekingpublicly traded.</p></div>
  <div class="reason" style="left:636px;top:420px"><span class="num">4.</span><h3>Registration &amp; Accreditation</h3><p>Given the increasing legal and regulatory complexity of today's business environment, many companies are faced with the choice of either committing</p></div>
</section>

<section class="testimonials">
  <div class="rule" style="left:350px"></div>
  <h2>Satisfied Customer</h2>
  <div class="rule" style="left:770px"></div>
  <div class="sub">We assume your satisfaction. We only finish work on your modern website if you are<br>completely satisfied with the result.</div>
  <div class="review" style="left:77px;width:311px"><div class="site">Halvenmark.de<span class="stars">★★★★★</span></div><div class="who-name">Tomas Reiner</div><p>Through the system, MP3, Streamora, Voxa Home and many other music system and platforms can be distributed throughout the house and served by it.</p></div>
  <div class="review" style="left:426px;width:326px"><div class="site">Halvenmark.de<span class="stars">★★★★★</span></div><div class="who-name">Tomas Reiner</div><p>Through the system, MP3, Streamora, Voxa Home and many other music system and platforms can be distributed throughout the house and served by it.</p></div>
  <div class="review" style="left:776px;width:328px"><div class="site">Halvenmark.de<span class="stars">★★★★★</span></div><div class="who-name">Tomas Reiner</div><p>Through the system, MP3, Streamora, Voxa Home and many other music system and platforms can be distributed throughout the house and served by it.</p></div>
  <div class="badge" style="left:311px;width:132px;height:89px"></div>
  <div class="badge" style="left:491px;width:84px;height:89px"></div>
  <div class="badge" style="left:611px;width:72px;height:72px;top:405px;border-radius:8px;background:#3a78c2"></div>
  <div class="badge" style="left:723px;width:163px;height:60px;top:410px;background:#2f6fc0"></div>
</section>

<footer class="site-footer">
  <div class="foot-logo">KORVALENDI</div>
  <p class="foot-about">Can a life insurance company deny a death benefit claim if they discover an applicant misrepresented key information when applying for coverage?</p>
  <div class="foot-col" style="left:512px"><h4>Company</h4><ul><li>Home</li><li>About</li><li>Services</li><li>Careers</li><li>FAQ</li><li>Blog</li><li>Contact</li></ul></div>
  <div class="foot-col" style="left:661px"><h4>Content</h4><ul><li>Our Mission</li><li>Disability Insurance</li><li>Get a Quote</li><li>Blog</li><li>FAQ</li><li>Privacy Policy</li><li>Sitemap</li></ul></div>
  <div class="foot-col" style="left:826px"><h4>Follow Us</h4><div class="foot-social"><span></span><span></span><span></span><span></span></div></div>
  <a class="newsletter">Newsletter Signup</a>
</footer>
<div class="footer-bottom">2018 All rights reserved</div>

</body>
</html>
```